Clerical Business Card Design

I have just started a new business focusing on Clerical / Administration Support for Small to Medium sized Businesses. I can provide support not just only my local area but anywhere as long as it is able to be done over the internet/email. I am the only person working in the business.
I would like to see some designs that are bright in colour yet a clean fresh design. The design should communicate balance.
Updates

Target Market(s)

Small to Medium sized Professional Businesses

Industry/Entity Type

Business

Contact Information for Business Card

Business Name: Vormley's Clerical
Statement: Providing Balanced Efficient Support
My Name: Ilsa Vormley
Phone: 0418 571 924 or 02 6519 4027
Email: vormleysclerical@plimmet.com.au

Colors

Designer to choose colors to be used in the design.

Requirements
Must have
• I'm open to suggestions
Nice to have
• I would like to see maybe something done with the two "C" in the business name whether that could be a focus of difference
Should not have
• Cartoon type pictures

```html
<!DOCTYPE html>
<html lang="en">
<head>
<meta charset="utf-8">
<title>Vormley's Clerical – Business Cards</title>
<link rel="stylesheet" href="https://fonts.googleapis.com/css2?family=Open+Sans:wght@400;600;700&display=swap">
<style>
  :root {
    --card-blue: #0a96de;
    --card-faint: #1ba5ea;
    --sun-yellow: #ffe01a;
    --fresh-green: #22f07a;
    --white: #ffffff;
    --stage-light: #ffffff;
    --stage-dark: #000000;
  }
  * { margin: 0; padding: 0; box-sizing: border-box; }
  html, body { width: 1200px; height: 1000px; overflow: hidden; }
  body {
    position: relative;
    background: var(--stage-light);
    font-family: "Open Sans", Arial, sans-serif;
  }
  .back-band {
    position: absolute; left: 0; top: 682px;
    width: 1200px; height: 318px;
    background: var(--stage-dark);
  }
  .card {
    position: absolute;
    background: var(--card-blue);
    overflow: hidden;
  }
  .card-front { top: 174px; width: 426px; height: 260px; }
  .card-front.is-yellow { left: 154px; --accent: var(--sun-yellow); }
  .card-front.is-green { left: 642px; --accent: var(--fresh-green); }
  .card-shade {
    position: absolute; top: 434px; width: 426px; height: 140px;
    background: linear-gradient(#e4e4e4, rgba(255,255,255,0));
  }
  .brand {
    position: absolute; left: 29px; top: 40px;
    display: flex; align-items: center; gap: 8px;
  }
  .brand-dot {
    width: 22px; height: 22px; border-radius: 50%;
    background: var(--accent);
  }
  .brand-name {
    color: var(--white); font-weight: 700; font-size: 22px; letter-spacing: 0.2px;
  }
  .tagline {
    position: absolute; left: 29px; top: 88px;
    color: var(--white); font-size: 11px;
  }
  .person-name {
    position: absolute; right: 66px; top: 154px;
    color: var(--accent); font-weight: 700; font-size: 23px; letter-spacing: 0.3px;
  }
  .contact-grid { position: absolute; left: 155px; top: 198px; width: 256px; height: 44px; }
  .contact-grid .rule { position: absolute; background: var(--white); }
  .rule-h { left: 0; top: 21px; width: 256px; height: 1px; }
  .rule-v1 { left: 13px; top: 0; width: 1px; height: 44px; }
  .rule-v2 { left: 66px; top: 0; width: 1px; height: 44px; }
  .contact-label, .contact-value { position: absolute; font-size: 11.5px; line-height: 16px; }
  .contact-label { left: 22px; color: var(--accent); }
  .contact-value { left: 81px; color: var(--white); white-space: nowrap; font-size: 11px; }
  .row-1 { top: 2px; }
  .row-2 { top: 25px; }
  .card-back { top: 732px; width: 357px; height: 218px; }
  .card-back.is-stacked { left: 224px; }
  .card-back.is-inline { left: 643px; }
  .faint-name, .faint-tagline { position: absolute; color: var(--card-faint); font-weight: 700; }
  .is-stacked .faint-name { left: 78px; top: 38px; font-size: 34px; line-height: 44px; }
  .is-stacked .faint-tagline { left: 58px; top: 172px; font-size: 12px; font-weight: 400; }
  .is-inline .faint-name { left: 0; right: 0; text-align: center; top: 78px; font-size: 28px; }
  .is-inline .faint-tagline { left: 0; right: 0; text-align: center; top: 134px; font-size: 13px; font-weight: 400; }
</style>
</head>
<body>
  <div class="back-band"></div>

  <div class="card card-front is-yellow">
    <div class="brand"><span class="brand-dot"></span><span class="brand-name">Vormley's Clerical</span></div>
    <p class="tagline">Providing Balanced Efficient Support</p>
    <p class="person-name">ILSA VORMLEY</p>
    <div class="contact-grid">
      <span class="rule rule-h"></span><span class="rule rule-v1"></span><span class="rule rule-v2"></span>
      <span class="contact-label row-1">Phone</span><span class="contact-value row-1">0418 571 924 / 02 65194027</span>
      <span class="contact-label row-2">Email</span><span class="contact-value row-2">vormleysclerical@plimmet.com.au</span>
    </div>
  </div>
  <div class="card-shade" style="left:154px"></div>

  <div class="card card-front is-green">
    <div class="brand"><span class="brand-dot"></span><span class="brand-name">Vormley's Clerical</span></div>
    <p class="tagline">Providing Balanced Efficient Support</p>
    <p class="person-name">ILSA VORMLEY</p>
    <div class="contact-grid">
      <span class="rule rule-h"></span><span class="rule rule-v1"></span><span class="rule rule-v2"></span>
      <span class="contact-label row-1">Phone</span><span class="contact-value row-1">0418 571 924 / 02 65194027</span>
      <span class="contact-label row-2">Email</span><span class="contact-value row-2">vormleysclerical@plimmet.com.au</span>
    </div>
  </div>
  <div class="card-shade" style="left:642px"></div>

  <div class="card card-back is-stacked">
    <p class="faint-name">Vormley's<br>Clerical</p>
    <p class="faint-tagline">Providing Balanced Efficient Support</p>
  </div>

  <div class="card card-back is-inline">
    <p class="faint-name">Vormley's Clerical</p>
    <p class="faint-tagline">Providing Balanced Efficient Support</p>
  </div>
</body>
</html>
```